Brightwell PC Help - Web Page
Remote Tech Support Provider
Brightwell PC Help - Web Page -
Creative Brief
24/7 remote PC support. Simple pricing and premium service supporting small business and consumers in the US.
Monthly service plans will be the emphasis but will also provide pay per incident support. Multiple computer discounts will be available and service plans will be structured as follows:
-- $19.99 for upto 3 computers
-- $34.99 for upto 5 computers
-- $79.00 for 10 computers
-- More than 10 computers, call for an instant quote.
KEY OFFERING:
* Automated UNLIMITED Online Backup as an add on for $5/month
Core focus will be on restoring the speed of your computer, removing viruses/malware etc. Will also help users with their WiFi Security Setup, printers, MP3 players, cameras, System Recovery Quillstone Suite, Email and Calendaring Setup, Domain Registration, Web Content Filtering Configuration,
Alternative Software Solution Recommendations... -- ALL for the same monthly fee.
MUST be 100% CSS for me to consider the submission. Prefer clean and simple over cluttered and complex. Every page will have a link that is up front and visible to take you to the order page.
www.vaultmerrow.example
www.helpquorn.example
www.dravelline.example

```html
<!DOCTYPE html>
<html lang="en">
<head>
<meta charset="utf-8">
<title>Brightwell PC Help</title>
<link href="https://fonts.googleapis.com/css2?family=Arimo:wght@400;700&display=swap" rel="stylesheet">
<style>
:root{
  --green:#7dbb2f;
  --orange:#f3901d;
  --red:#d9401c;
  --ink:#333;
  --muted:#666;
  --dark:#3a3a3a;
  --darker:#222;
  --hero-top:#ffffff;
  --hero-bottom:#e2e2e2;
  --line:#d0d0d0;
}
*{margin:0;padding:0;box-sizing:border-box}
html,body{width:1200px;height:842px;overflow:hidden}
body{font-family:"Arimo",Arial,sans-serif;color:var(--ink);background:#fff;font-size:12px;position:relative}
.wrap{position:absolute;left:205px;width:790px}

.topbar{position:absolute;top:0;left:0;width:1200px;height:30px}
.topbar .links{right:205px;left:auto;top:9px;font-size:11px;color:var(--muted);text-align:right}
.topbar a{color:var(--red);text-decoration:none}

.header{position:absolute;top:30px;left:0;width:1200px;height:66px;background:#fff}
.brand{top:13px;width:240px;display:flex;align-items:center;gap:8px}
.brand .mark{width:26px;height:26px;background:var(--green);flex:none}
.brand .name{font-size:18px;font-weight:700;color:var(--green);white-space:nowrap}
.nav{position:absolute;top:6px;right:205px;display:flex;height:48px}
.nav a{display:flex;align-items:center;padding:0 15px;font-size:10.5px;font-weight:700;color:#444;text-decoration:none;border-left:1px solid #e6e6e6;white-space:nowrap}
.nav a.active{background:linear-gradient(#f2f2f2,#d8d8d8);border-top:3px solid var(--green)}

.hero{position:absolute;top:96px;left:0;width:1200px;height:204px;background:linear-gradient(var(--hero-top),var(--hero-bottom))}
.prices{top:12px;list-style:none;width:360px}
.prices li{display:flex;align-items:center;gap:10px;font-size:17px;color:#555;height:26px;white-space:nowrap}
.prices li.quote{padding-left:30px;color:var(--orange)}
.prices .g{color:var(--green);font-size:19px}
.prices .o{color:var(--orange);font-size:19px}
.btn{position:absolute;top:163px;left:0;width:197px;height:34px;border-radius:17px;background:linear-gradient(#f4f4f4,#c9c9c9);border:1px solid #aaa;display:flex;align-items:center;justify-content:center;gap:10px;font-weight:700;font-size:14px;color:#333;text-decoration:none}
.hero-art{position:absolute;top:10px;left:443px;width:360px;height:180px;border-radius:8px;background:radial-gradient(ellipse at center,#9fb3c8 0%,#c9d3de 45%,rgba(226,226,226,0) 75%)}

.features{position:absolute;top:300px;left:0;width:1200px;height:79px;background:linear-gradient(#4a4a4a,#2d2d2d)}
.features .wrap{display:flex;justify-content:space-around;top:14px}
.feature{display:flex;gap:12px;width:220px;color:#ddd}
.feature .ico{width:46px;height:46px;flex:none}
.feature h3{font-size:13px;color:#fff;margin:4px 0 3px}
.feature p{font-size:10px;line-height:1.3;color:#bbb}

.intro{top:390px;width:670px;font-size:11.5px;line-height:1.45;color:#444}
.intro p{margin-bottom:12px}
.signin{position:absolute;top:396px;left:885px;width:110px;height:124px;border:1px solid var(--line);border-radius:4px;background:#f7f7f7;font-size:8.5px;color:#555;padding:0 6px}
.signin h4{margin:0 -6px 8px;padding:4px 6px;background:var(--dark);color:#fff;font-size:9px;border-radius:3px 3px 0 0}
.signin .row{display:flex;align-items:center;justify-content:space-between;margin-bottom:8px;white-space:nowrap}
.signin .field{width:50px;height:13px;border:1px solid #bbb;background:#fff}
.signin .go{display:block;width:38px;height:14px;border-radius:3px;background:var(--dark);color:#fff;font-size:8px;text-align:center;line-height:14px}

.services{top:606px;width:790px;display:flex;gap:35px}
.service{width:240px}
.service h3{font-size:9.5px;color:var(--red);font-weight:700;white-space:nowrap}
.service .sub{font-size:8.5px;color:var(--orange);margin:2px 0 4px;white-space:nowrap;overflow:hidden}
.service .photo{height:100px;border:1px solid #ccc}
.service p{font-size:9px;line-height:1.3;color:#555;margin-top:6px;height:25px;overflow:hidden}
.service a{font-size:9px;font-weight:700;color:#333;text-decoration:none}
.p1{background:linear-gradient(135deg,#8e1e14,#d24a2e 50%,#6b6b6b)}
.p2{background:linear-gradient(135deg,#3f6b86,#a8c4d8 50%,#597f99)}
.p3{background:linear-gradient(135deg,#9a9a9a,#f0f0f0 50%,#7c7c7c)}

.footer{position:absolute;top:804px;left:0;width:1200px;height:38px;background:var(--darker);color:#bbb;font-size:10px}
.footer .wrap{top:13px;display:flex;justify-content:space-between}
.footer b{color:#fff}
.footer a{color:#bbb;text-decoration:none}
</style>
</head>
<body>
<div class="topbar">
  <div class="wrap links"><a href="#">Log in</a> | <a href="#">Remote Access</a> | <a href="#">Register</a> | <a href="#">Support</a></div>
</div>

<header class="header">
  <div class="wrap brand"><span class="mark"></span><span class="name">Brightwell PC Help</span></div>
  <nav class="nav">
    <a class="active" href="#">HOME</a><a href="#">WHO WE ARE</a><a href="#">HOW IT WORKS</a><a href="#">PRODUCTS</a><a href="#">BUY</a><a href="#">NEWS</a><a href="#">CONTACT</a>
  </nav>
</header>

<section class="hero">
  <div class="wrap" style="top:0;height:204px">
    <ul class="prices">
      <li><svg width="20" height="14" viewBox="0 0 20 14"><path d="M1 10 Q6 3 13 4 V0 L19 6 L13 12 V8 Q7 7 1 10Z" fill="#f3901d"/></svg>$19.99 for upto <span class="g">3 computers</span></li>
      <li><svg width="20" height="14" viewBox="0 0 20 14"><path d="M1 10 Q6 3 13 4 V0 L19 6 L13 12 V8 Q7 7 1 10Z" fill="#f3901d"/></svg>$34.99 for upto <span class="o">5 computers</span></li>
      <li><svg width="20" height="14" viewBox="0 0 20 14"><path d="M1 10 Q6 3 13 4 V0 L19 6 L13 12 V8 Q7 7 1 10Z" fill="#f3901d"/></svg>$79.00 for 10 computers</li>
      <li><svg width="20" height="14" viewBox="0 0 20 14"><path d="M1 10 Q6 3 13 4 V0 L19 6 L13 12 V8 Q7 7 1 10Z" fill="#f3901d"/></svg>More than 10 computers</li>
      <li class="quote">call for an&nbsp;<span class="o">instant quote.</span></li>
    </ul>
    <a class="btn" href="#">GET STARTED HERE <svg width="14" height="14" viewBox="0 0 14 14"><circle cx="7" cy="7" r="7" fill="#333"/><path d="M5 4 L9 7 L5 10Z" fill="#fff"/></svg></a>
    <div class="hero-art" role="img" aria-label="Laptops and desktop computers networked around a central server"></div>
  </div>
</section>

<section class="features">
  <div class="wrap">
    <div class="feature">
      <svg class="ico" viewBox="0 0 46 46"><circle cx="23" cy="23" r="21" fill="#f3901d" stroke="#fff" stroke-width="2"/><text x="23" y="30" text-anchor="middle" font-size="20" font-weight="700" fill="#fff" font-family="Arimo,Arial,sans-serif">$</text></svg>
      <div><h3>Save big with us</h3><p>Lorem ipsum dolor sit amet consectetur adipiscing elit.</p></div>
    </div>
    <div class="feature">
      <svg class="ico" viewBox="0 0 46 46"><circle cx="23" cy="23" r="21" fill="#f3901d" stroke="#fff" stroke-width="2"/><circle cx="23" cy="23" r="14" fill="#fff"/><path d="M23 13 V23 L30 27" stroke="#333" stroke-width="2" fill="none"/></svg>
      <div><h3>Always on time</h3><p>Lorem ipsum dolor sit amet consectetur adipiscing elit.</p></div>
    </div>
    <div class="feature">
      <svg class="ico" viewBox="0 0 46 46"><circle cx="23" cy="23" r="21" fill="#f3901d" stroke="#fff" stroke-width="2"/><path d="M15 14 Q13 24 22 31 Q28 35 32 32 L29 27 L25 28 Q20 24 19 20 L21 17Z" fill="#fff"/></svg>
      <div><h3>Contact Us</h3><p>Lorem ipsum dolor sit amet consectetur adipiscing elit.</p></div>
    </div>
  </div>
</section>

<main>
  <div class="wrap intro">
    <p>Monthly service plans will be the emphasis but will also provide pay per incident support. Multiple computer discounts will be available and service plans will be structured as follows:</p>
    <p>Lorem ipsum dolor sit amet, consectetur adipiscing elit. Aenean dignissim nibh vel ipsum venenatis eget sollicitudin augue aliquet. Class aptent taciti sociosqu ad litora torquent per conubia nostra, per inceptos himenaeos. Quisque aliquet, orci ut facilisis bibendum, massa massa viverra massa, eu hendrerit justo quam in leo. Sed scelerisque nibh at massa molestie eu convallis dolor porttitor.</p>
    <p>In in felis eget enim aliquet malesuada nec ac magna. Suspendisse potenti. Etiam tincidunt iaculis nisi, et vehicula purus porta vitae. Vestibulum ante ipsum primis in faucibus orci luctus et ultrices posuere cubilia.</p>
  </div>

  <form class="signin">
    <h4>Sign in</h4>
    <div class="row">User Name <span class="field"></span></div>
    <div class="row">Password <span class="field"></span></div>
    <div class="row">Email <span class="field"></span></div>
    <div class="row"><span>&#9633; Login only</span><span class="go">Log in</span></div>
  </form>

  <div class="wrap services">
    <article class="service">
      <h3>Removing viruses/malware</h3>
      <div class="sub">Pellentesque habitant morbi tristique senectus</div>
      <div class="photo p1" role="img" aria-label="Close-up of a keyboard with a red virus key"></div>
      <p>Lorem ipsum dolor sit amet, consectetur adipiscing elit. Aenean commodo ligula eget dolor.</p>
      <a href="#">Read more »</a>
    </article>
    <article class="service">
      <h3>WiFi Security Setup</h3>
      <div class="sub">Nullam tellus et ligula sed porta</div>
      <div class="photo p2" role="img" aria-label="Blue digital network security scene"></div>
      <p>Fusce vel cursus vestibulum sollicitudin nisl in mauris imperdiet pretium sed ut dolor.</p>
      <a href="#">Read more »</a>
    </article>
    <article class="service">
      <h3>Alternative Software Solution Recommendations</h3>
      <div class="sub">Donec quis lectus sit amet</div>
      <div class="photo p3" role="img" aria-label="Grey puzzle pieces fitting together"></div>
      <p>Donec quis elit eget nunc suscipit sit amet non purus lorem, sed malesuada tempus dolor.</p>
      <a href="#">Read more »</a>
    </article>
  </div>
</main>

<footer class="footer">
  <div class="wrap">
    <span>Copyright © 2011, <b>Brightwell PC Help</b>. All rights reserved</span>
    <span><a href="#">Home</a> | <a href="#">Who we are</a> | <a href="#">How it Works</a> | <a href="#">Products</a> | <a href="#">Buy</a> | <a href="#">News</a> | <a href="#">Contact</a></span>
  </div>
</footer>
</body>
</html>
```